BOLD & MINIMALIST DESIGN NEEDED

We want a very bold but minimalistic business card design that is impactful and utilizes both sides of the business card. Our current logo is included for your use.

We want bold fonts and good use of negative space. We don't want the logo to overpower the design.

Target Market(s)

Professionals who are building new commercial buildings.

Industry/Entity Type

Construction

Contact Information for Business Card

Name, Title, email, office phone, cell phone, website

Font styles to use
Serif
Sans Serif

Requirements
Must have
• Bold design!

```html
<!DOCTYPE html>
<html lang="en">
<head>
<meta charset="utf-8">
<title>Ridgecrest Business Card</title>
<link rel="stylesheet" href="https://fonts.googleapis.com/css2?family=Roboto:wght@400;700;900&display=swap">
<style>
  :root {
    --page-bg: #e6e6e6;
    --card-white: #f4f4f5;
    --ink: #111213;
    --text: #222324;
    --green: #7cb82a;
    --green-light: #b2d87c;
    --divider: #cfcfcf;
  }
  * { margin: 0; padding: 0; box-sizing: border-box; }
  html, body {
    width: 1200px;
    height: 1040px;
    overflow: hidden;
    background: var(--page-bg);
    font-family: "Roboto", Arial, sans-serif;
  }
  .canvas {
    position: relative;
    width: 1200px;
    height: 1040px;
  }
  .card {
    position: absolute;
    left: 280px;
    width: 640px;
    height: 366px;
    border-radius: 16px;
    overflow: hidden;
  }
  .card--front { top: 130px; background: var(--card-white); }
  .card--back {
    top: 568px;
    background: radial-gradient(ellipse 55% 60% at 50% 48%, var(--green-light) 0%, #9ccb55 55%, var(--green) 100%);
  }

  /* front: brand block */
  .brand {
    position: absolute;
    left: 40px;
    top: 158px;
    width: 250px;
    display: flex;
    align-items: center;
    justify-content: center;
    gap: 10px;
  }
  .brand__square {
    width: 18px;
    height: 18px;
    background: var(--green);
  }
  .brand__name {
    font-weight: 900;
    font-size: 30px;
    letter-spacing: 0.5px;
    color: var(--ink);
  }
  .divider {
    position: absolute;
    left: 322px;
    top: 102px;
    width: 1px;
    height: 184px;
    background: var(--divider);
  }

  /* front: contact block */
  .contact {
    position: absolute;
    left: 339px;
    top: 105px;
    color: var(--text);
  }
  .contact__name {
    font-weight: 700;
    font-size: 26px;
    line-height: 1.1;
    color: var(--ink);
  }
  .contact__title {
    font-size: 16px;
    color: var(--green);
    margin: 2px 0 0 1px;
  }
  .contact__address {
    font-size: 16px;
    line-height: 20px;
    margin-top: 12px;
  }
  .contact__list {
    list-style: none;
    margin-top: 12px;
    font-size: 16px;
    line-height: 20px;
  }
  .contact__list li { display: flex; align-items: center; gap: 8px; }
  .contact__icon { width: 13px; height: 13px; flex: none; }

  /* back */
  .back__name {
    position: absolute;
    left: 0;
    right: 0;
    top: 140px;
    text-align: center;
    font-weight: 900;
    font-size: 56px;
    letter-spacing: 1px;
    color: var(--ink);
  }
  .back__web {
    position: absolute;
    left: 0;
    right: 0;
    top: 310px;
    text-align: center;
    font-size: 15px;
    color: var(--text);
  }
</style>
</head>
<body>
<main class="canvas">
  <section class="card card--front" aria-label="Business card front">
    <div class="brand">
      <span class="brand__square"></span>
      <span class="brand__name">RIDGECREST</span>
    </div>
    <div class="divider"></div>
    <div class="contact">
      <h1 class="contact__name">OWEN HARTLEY</h1>
      <p class="contact__title">President</p>
      <p class="contact__address">2170 Carver Lane<br>Oak Hollow, NY 11420</p>
      <ul class="contact__list">
        <li>
          <svg class="contact__icon" viewBox="0 0 16 16" aria-hidden="true"><path fill="#111213" d="M3.5 1 6 3.5 4.6 5.6c.9 2.2 3.6 4.9 5.8 5.8L12.5 10 15 12.5l-1.9 2.4C7.8 14.6 1.4 8.2 1.1 2.9z"/></svg>
          <span>(555) 0142-7788</span>
        </li>
        <li>
          <svg class="contact__icon" viewBox="0 0 16 16" aria-hidden="true"><rect x="1" y="3.5" width="14" height="9" fill="#111213"/><path d="M1.5 4 8 9l6.5-5" fill="none" stroke="#f4f4f5" stroke-width="1.2"/></svg>
          <span>info@ridgecrestbuild.com</span>
        </li>
        <li>
          <svg class="contact__icon" viewBox="0 0 16 16" aria-hidden="true"><circle cx="8" cy="8" r="7" fill="#111213"/><path d="M4 5c2 0 2 2 3.5 2.5S7 11 8.5 12M10 3c0 2 2 2 3 3" fill="none" stroke="#f4f4f5" stroke-width="1.3"/></svg>
          <span>www.ridgecrestbuild.com</span>
        </li>
      </ul>
    </div>
  </section>

  <section class="card card--back" aria-label="Business card back">
    <p class="back__name">RIDGECREST</p>
    <p class="back__web">www.ridgecrestbuild.com</p>
  </section>
</main>
</body>
</html>
```